Landing Page that will convert (Design Only Landing Page Project)

I am looking for a design that will resonate with a dentist, doctor or anyone business owner in the medical field. My goal is to have then scheduled a 15 min session with me at the end to discuss how I can help then meet there financial goals (short or long term)

I am open to all design concepts and suggestions as far as the important contents or links that should be on the page (ie. Main menu like, Home, About, Services, Schedule, Contact Us).

There is no right or wrong answer, just need a great accounting/financing landing page. Again the project is for just the design of the page, and coding will be done elsewhere.

Target Market(s)

medical professionals, this includes small business owners of privately held office suck as medical doctors, dentist, ophthalmologist, chiropractors, etc

Industry/Entity Type

Finance And Accounting

Colors
fdfdfd
1b1b1b
f3f1f8
e4daeb

Requirements
Must have
• The goal of this landing page is to have the visitor schedule a 15min discovery call, therefore, a calender scheduling option is ideal, so we can understand their goals and see what obstacles they are facing and therefore avoid those obstacles before they become a burden
Nice to have
• A video background or maybe a medical professional office in that way they feel connected. For design purposes just use a video/image placeholder. I feel more is less if we can research some of the most successful landing page design and incorporate some of those elements that would to great.
• I saw this example and thought it was ok
• https://www.plovanet.com/#features
• WHAT I LIKE ABOUT THIS DESIGN:
• - It's simple, clean,
• - font is readable,
• - like the illustration
• - elegance
• - It clearly defines what the use should do, its intuitive, walks the user to the bottom of the page and give them the option of whether to signup or exit the page.

```html
<!DOCTYPE html>
<html lang="en">
<head>
<meta charset="utf-8">
<title>Steady Ledger — Financial Goals for Medical Practices</title>
<link rel="stylesheet" href="https://fonts.googleapis.com/css2?family=Questrial&family=Lato:ital,wght@0,400;0,700;0,900;1,400&display=swap">
<style>
:root{
  --plum:#4b2c4a;
  --plum-deep:#3a1f39;
  --plum-soft:#6d4a6b;
  --lavender:#e4daeb;
  --lavender-pale:#f3f1f8;
  --white:#fdfdfd;
  --ink:#1b1b1b;
  --text:#555;
  --gold:#e6b422;
}
*{box-sizing:border-box;margin:0;padding:0}
html,body{width:1200px;height:4167px;overflow:hidden}
body{position:relative;background:var(--white);font-family:"Lato",sans-serif;color:var(--text)}
.abs{position:absolute}
h1,h2,h3,.brand,.nav a{font-family:"Questrial",sans-serif}
.section-title{position:absolute;left:0;width:1200px;text-align:center;font-size:38px;color:var(--ink);font-weight:400}
.btn{position:absolute;display:flex;align-items:center;justify-content:center;font-family:"Lato",sans-serif;font-size:18px;letter-spacing:.5px;text-transform:uppercase;border-radius:4px}
.btn-light{background:var(--white);color:var(--plum)}
.btn-dark{background:var(--plum);color:var(--white)}
.photo{position:absolute;background:linear-gradient(135deg,#d9cfdc,#b8a3b9 55%,#8e7390)}

/* hero */
.hero-bg{position:absolute;left:0;top:0}
.brand{position:absolute;left:78px;top:30px;font-size:34px;color:var(--white);letter-spacing:.5px}
.nav{position:absolute;top:39px;left:425px;display:flex;gap:32px;font-size:16px}
.nav a{color:var(--white);text-decoration:none;white-space:nowrap}
.nav a.active{border-top:3px solid var(--white);padding-top:8px;margin-top:-11px}
.search{position:absolute;left:878px;top:39px}
.btn-book{left:925px;top:22px;width:197px;height:53px;font-family:"Questrial",sans-serif;font-size:19px;text-transform:uppercase;border-radius:3px}
.hero-title{position:absolute;left:78px;top:176px;font-size:52px;line-height:62px;color:var(--white);font-weight:700;letter-spacing:1px}
.hero-text{position:absolute;left:78px;top:311px;width:470px;font-size:16px;line-height:26px;color:#f1e8f0}
.btn-contact{left:78px;top:397px;width:155px;height:50px}
.hero-photo{left:542px;top:111px;width:583px;height:529px;border-radius:140px 40px 140px 40px}

/* help */
.help-item{position:absolute;width:330px;text-align:center;font-size:22px;line-height:31px;color:#6a6a6a}
.help-item strong{color:var(--ink);font-weight:700}
.help-icon{position:absolute;width:112px;height:112px;border-radius:50%;background:var(--lavender);display:flex;align-items:center;justify-content:center}
.help-icon.active{background:var(--plum)}

/* services */
.service{position:absolute;top:1217px;width:333px;text-align:center}
.service .photo{position:relative;width:333px;height:191px;border-radius:16px}
.service h3{margin-top:38px;font-family:"Lato",sans-serif;font-weight:700;font-size:19px;color:var(--ink);letter-spacing:.3px}
.service p{margin-top:14px;font-size:15px;line-height:22px;color:#666;padding:0 8px}

/* about */
.about-photo{border:3px solid var(--white);box-shadow:0 6px 18px rgba(60,30,60,.25)}
.about-title{position:absolute;left:733px;top:1866px;font-size:38px;color:var(--ink);font-weight:400}
.about-text{position:absolute;left:733px;width:390px;font-size:16px;line-height:29px;color:#666}

/* testimonials */
.quote-card{position:absolute;top:2611px;width:500px;height:139px;border:2px solid #ddd;background:var(--white);padding:26px 30px 0 74px;font-size:15px;line-height:24px;color:#555}
.quote-mark{position:absolute;left:24px;top:14px;font-family:"Lato",sans-serif;font-weight:900;font-size:64px;line-height:64px;color:var(--plum)}
.avatar{position:absolute;top:2789px;width:105px;height:105px;border-radius:50%;border:4px solid var(--plum);background:linear-gradient(160deg,#e9e2ea,#b9a6ba)}
.client{position:absolute;top:2805px}
.client b{display:block;font-family:"Questrial",sans-serif;font-size:23px;color:var(--ink);font-weight:400}
.client span{display:block;font-size:14px;color:#777;margin-top:4px}
.client i{display:block;font-style:normal;color:var(--gold);font-size:15px;letter-spacing:1px}
.dots{position:absolute;top:2922px;left:560px;display:flex;gap:14px}
.dots span{width:14px;height:14px;border:1px solid #bbb}
.dots span.on{background:var(--plum);border-color:var(--plum)}

/* newsletter */
.sub-line{position:absolute;left:0;top:3070px;width:1200px;text-align:center;font-style:italic;font-size:17px;color:#666}
.subscribe{position:absolute;left:258px;top:3133px;width:681px;height:61px;border-radius:31px;background:var(--white);box-shadow:0 4px 16px rgba(60,30,60,.25);overflow:hidden;display:flex}
.subscribe .field{flex:1;display:flex;align-items:center;gap:12px;padding-left:30px;font-style:italic;font-size:17px;color:#666}
.subscribe .go{width:160px;background:var(--plum);color:var(--white);display:flex;align-items:center;justify-content:center;font-size:18px;letter-spacing:.5px}

/* contact */
.contact-item{position:absolute;top:3490px;width:330px;text-align:center;font-size:17px;line-height:28px;color:#444}
.contact-item svg{display:block;margin:0 auto 16px}
.form-field{position:absolute;border:1px solid #d7d7d7;background:var(--white);font-size:15px;color:#555;padding:0 12px;display:flex;align-items:center;justify-content:space-between}
.form-field.area{align-items:flex-start;padding-top:18px}
.btn-appoint{left:472px;top:3978px;width:259px;height:61px;font-size:18px;gap:14px;border-radius:3px}

/* footer */
.footer{position:absolute;left:0;top:4103px;width:1200px;height:64px;background:var(--plum-deep);color:#e8dce7;font-size:14px;display:flex;align-items:center;padding-left:78px}
.footer b{color:var(--white)}
.social{position:absolute;top:19px;width:35px;height:35px;border-radius:50%;border:2px solid var(--white)}
</style>
</head>
<body>

<!-- HERO -->
<svg class="hero-bg" width="1200" height="690" viewBox="0 0 1200 690" aria-hidden="true">
  <defs>
    <linearGradient id="heroGrad" x1="0" y1="0" x2="1" y2="1">
      <stop offset="0" stop-color="#5a3658"/>
      <stop offset="1" stop-color="#3c213b"/>
    </linearGradient>
  </defs>
  <rect width="1200" height="690" fill="var(--white)"/>
  <path d="M0 0H1200V600C1080 640 960 560 760 620C560 680 300 640 0 690Z" fill="url(#heroGrad)"/>
  <path d="M260 0C320 120 300 260 420 380C520 480 540 600 470 690H1200V0Z" fill="#7a5a79" opacity=".25"/>
  <path d="M520 0C500 160 560 300 530 420C500 560 620 640 760 690H1200V0Z" fill="#a48ca4" opacity=".22"/>
  <path d="M0 560C200 600 420 560 620 610C820 660 1000 600 1200 640V690H0Z" fill="var(--white)"/>
</svg>

<div class="brand">steady ledger</div>
<nav class="nav">
  <a class="active">Home</a><a>About</a><a>Services</a><a>Schedule</a><a>Contact Us</a>
</nav>
<svg class="search" width="18" height="18" viewBox="0 0 18 18" aria-hidden="true"><circle cx="7.5" cy="7.5" r="6" fill="none" stroke="#d8c8d7" stroke-width="2"/><path d="M12 12l5 5" stroke="#d8c8d7" stroke-width="2"/></svg>
<div class="btn btn-light btn-book">Book a Schedule</div>

<h1 class="hero-title">Steady Ledger<br>Financial Goals</h1>
<p class="hero-text">Lorem ipsum dolor sit amet, consectetur adipiscing elit, sed do eiusmod tempor incididunt ut labore et dolore magna aliqua.</p>
<div class="btn btn-light btn-contact">Contact Us</div>
<div class="photo hero-photo" role="img" aria-label="Photo of a smiling dental patient holding a clear aligner"></div>

<!-- HOW TO HELP -->
<h2 class="section-title" style="top:692px">How to help You</h2>

<div class="help-icon" style="left:183px;top:772px">
  <svg width="54" height="50" viewBox="0 0 54 50" aria-hidden="true" fill="none" stroke="var(--plum)" stroke-width="3"><rect x="8" y="4" width="38" height="24" rx="2"/><path d="M27 28v8M4 44h46M16 36h22"/></svg>
</div>
<div class="help-icon active" style="left:541px;top:772px">
  <svg width="56" height="52" viewBox="0 0 56 52" aria-hidden="true" fill="none" stroke="var(--white)" stroke-width="3"><rect x="4" y="8" width="48" height="40" rx="4"/><path d="M4 18h48M16 3v10M40 3v10"/><g fill="var(--white)" stroke="none"><rect x="12" y="24" width="6" height="5"/><rect x="25" y="24" width="6" height="5"/><rect x="38" y="24" width="6" height="5"/><rect x="12" y="35" width="6" height="5"/><rect x="25" y="35" width="6" height="5"/><rect x="38" y="35" width="6" height="5"/></g></svg>
</div>
<div class="help-icon" style="left:902px;top:772px">
  <svg width="44" height="54" viewBox="0 0 44 54" aria-hidden="true" fill="none" stroke="var(--plum)" stroke-width="3"><path d="M6 3h24l10 10v38H6z"/><path d="M30 3v10h10M13 24h18M13 32h18M13 40h12"/></svg>
</div>

<p class="help-item" style="left:74px;top:915px">The Goals is to have the visitor schedule a 15min discovery call</p>
<p class="help-item" style="left:432px;top:915px"><strong>A calender scheduling option is ideal, so we can understand their goals</strong></p>
<p class="help-item" style="left:793px;top:915px">See what obstacles they are facing and therefore avoid those obstacles before they become a burden</p>

<svg class="abs" style="left:0;top:1040px" width="1200" height="90" viewBox="0 0 1200 90" aria-hidden="true"><path d="M0 60C300 20 500 90 800 50C1000 25 1120 40 1200 30V90H0Z" fill="var(--lavender-pale)" opacity=".7"/></svg>

<!-- SERVICES -->
<h2 class="section-title" style="top:1128px">Our Services</h2>

<div class="service" style="left:78px">
  <div class="photo" role="img" aria-label="Photo of a dentist with a young patient"></div>
  <h3>LOREM IPSUM DOLOR SIT AMET</h3>
  <p>Lorem ipsum dolor sit amet, consectetur adipiscing elit, sed do eiusmod tempor incididunt ut labore et dolore magna aliqua.</p>
</div>
<div class="service" style="left:433px">
  <div class="photo" role="img" aria-label="Photo of a patient during a dental check-up"></div>
  <h3>LOREM IPSUM DOLOR SIT AMET</h3>
  <p>Lorem ipsum dolor sit amet, consectetur adipiscing elit, sed do eiusmod tempor incididunt ut labore et dolore magna aliqua.</p>
</div>
<div class="service" style="left:789px">
  <div class="photo" role="img" aria-label="Photo of a family with their dentist"></div>
  <h3>LOREM IPSUM DOLOR SIT AMET</h3>
  <p>Lorem ipsum dolor sit amet, consectetur adipiscing elit, sed do eiusmod tempor incididunt ut labore et dolore magna aliqua.</p>
</div>

<svg class="abs" style="left:0;top:1580px" width="1200" height="240" viewBox="0 0 1200 240" aria-hidden="true">
  <path d="M0 20C250 -10 420 90 700 70C940 52 1080 10 1200 30V240H0Z" fill="var(--lavender)" opacity=".55"/>
  <path d="M0 60C260 30 460 120 720 100C950 82 1090 40 1200 60V240H0Z" fill="var(--lavender-pale)"/>
  <path d="M0 180C300 130 520 210 800 190C980 176 1110 200 1200 190V240H0Z" fill="var(--white)"/>
</svg>
<div class="btn btn-dark" style="left:536px;top:1572px;width:125px;height:50px;font-size:17px">View All</div>

<!-- ABOUT -->
<div class="photo about-photo" style="left:78px;top:1806px;width:291px;height:258px;border-radius:90px 20px 90px 20px" role="img" aria-label="Photo of colleagues meeting around a table"></div>
<div class="photo about-photo" style="left:389px;top:1897px;width:292px;height:256px;border-radius:20px 90px 20px 90px" role="img" aria-label="Photo of a handshake over a desk with a stethoscope"></div>
<div class="photo about-photo" style="left:78px;top:2089px;width:291px;height:267px;border-radius:20px 90px 20px 90px" role="img" aria-label="Photo of a medical team holding a tablet"></div>

<h2 class="about-title">About Steady Ledger</h2>
<p class="about-text" style="top:1933px">Lorem ipsum dolor sit amet, consectetur adipiscing elit, sed do eiusmod tempor incididunt ut labore et dolore magna aliqua. Ut enim ad minim veniam, quis nostrud exercitation ullamco laboris nisi ut aliquip ex ea commodo consequat.</p>
<p class="about-text" style="top:2092px">Lorem ipsum dolor sit amet, consectetur adipiscing elit, sed do eiusmod tempor incididunt ut labore et dolore magna aliqua. Ut enim ad minim veniam, quis nostrud exercitation ullamco laboris nisi ut aliquip ex ea commodo consequat. Duis aute irure dolor in reprehenderit in voluptate velit esse cillum dolore eu fugiat nulla pariatur.</p>

<svg class="abs" style="left:0;top:2350px" width="1200" height="160" viewBox="0 0 1200 160" aria-hidden="true">
  <path d="M0 40C280 110 560 20 820 50C1000 70 1120 30 1200 20V160H0Z" fill="var(--lavender)" opacity=".55"/>
  <path d="M0 90C300 140 560 60 840 90C1010 108 1130 80 1200 70V160H0Z" fill="var(--lavender-pale)"/>
  <path d="M0 140C300 160 600 110 900 130C1040 140 1140 130 1200 128V160H0Z" fill="var(--white)"/>
</svg>

<!-- TESTIMONIALS -->
<h2 class="section-title" style="top:2525px">Client Testimonial</h2>

<div class="quote-card" style="left:78px"><span class="quote-mark">&ldquo;</span>Lorem Ipsum is simply dummy text of the printing and typesetting industry. Lorem Ipsum has been the industry's standard dummy text ever since the 1500s.</div>
<div class="quote-card" style="left:620px"><span class="quote-mark">&ldquo;</span>Lorem Ipsum is simply dummy text of the printing and typesetting industry. Lorem Ipsum has been the industry's standard dummy text ever since the 1500s.</div>

<div class="avatar" style="left:78px" role="img" aria-label="Client portrait"></div>
<div class="client" style="left:197px"><b>Marla Quinn</b><span>California</span><i>★★★★☆</i></div>
<div class="avatar" style="left:620px" role="img" aria-label="Client portrait"></div>
<div class="client" style="left:740px"><b>Devon Reyes</b><span>California</span><i>★★★★☆</i></div>

<div class="dots"><span></span><span class="on"></span><span></span><span></span></div>

<!-- NEWSLETTER -->
<h2 class="section-title" style="top:3005px">Subscribe Newsletter</h2>
<p class="sub-line">Lorem Ipsum is simply dummy text of the printing and typesetting industry.</p>
<div class="subscribe">
  <div class="field"><svg width="20" height="14" viewBox="0 0 20 14" aria-hidden="true"><rect width="20" height="14" fill="var(--plum)"/><path d="M0 0l10 8 10-8" fill="none" stroke="var(--white)" stroke-width="1.5"/></svg>Enter Email :</div>
  <div class="go">SUBSCRIBE</div>
</div>

<svg class="abs" style="left:0;top:3225px" width="1200" height="160" viewBox="0 0 1200 160" aria-hidden="true">
  <path d="M0 60C300 0 560 90 820 60C1000 40 1120 10 1200 20V160H0Z" fill="var(--lavender)" opacity=".55"/>
  <path d="M0 100C300 50 560 120 840 100C1010 88 1130 60 1200 60V160H0Z" fill="var(--lavender-pale)"/>
  <path d="M0 150C300 120 600 160 900 140C1040 130 1140 140 1200 138V160H0Z" fill="var(--white)"/>
</svg>

<!-- CONTACT -->
<h2 class="section-title" style="top:3402px">Contact Us</h2>

<div class="contact-item" style="left:79px">
  <svg width="26" height="34" viewBox="0 0 26 34" aria-hidden="true"><path d="M13 1C6 1 1 6 1 13c0 9 12 20 12 20s12-11 12-20C25 6 20 1 13 1z" fill="none" stroke="#333" stroke-width="2.5"/><circle cx="13" cy="13" r="4" fill="#333"/></svg>
  4180 Harbor Road West<br>Brookfield, TX 79001
</div>
<div class="contact-item" style="left:432px">
  <svg width="22" height="34" viewBox="0 0 22 34" aria-hidden="true"><rect x="2" y="1" width="18" height="32" rx="3" fill="none" stroke="#333" stroke-width="2.5"/><circle cx="11" cy="27" r="1.8" fill="#333"/></svg>
  555.201.4400 , 555.201.4410
</div>
<div class="contact-item" style="left:788px">
  <svg width="40" height="30" viewBox="0 0 40 30" aria-hidden="true"><rect x="1.5" y="1.5" width="37" height="27" fill="none" stroke="#333" stroke-width="2.5"/><path d="M2 3l18 14 18-14" fill="none" stroke="#333" stroke-width="2.5"/></svg>
  info@steadyledger.com
</div>

<div class="form-field" style="left:289px;top:3633px;width:622px;height:61px">Full Name* :</div>
<div class="form-field" style="left:289px;top:3706px;width:303px;height:61px">Email Address* :</div>
<div class="form-field" style="left:606px;top:3706px;width:305px;height:61px">Phone Number* :</div>
<div class="form-field" style="left:289px;top:3778px;width:303px;height:61px">dd / mm/ yyyy :
  <svg width="16" height="16" viewBox="0 0 16 16" aria-hidden="true"><rect x="1" y="3" width="14" height="12" fill="none" stroke="#444" stroke-width="1.5"/><path d="M1 7h14M5 1v4M11 1v4" stroke="#444" stroke-width="1.5"/></svg></div>
<div class="form-field" style="left:606px;top:3778px;width:305px;height:61px">8:00 a.m - 9:00 p.m :
  <svg width="16" height="16" viewBox="0 0 16 16" aria-hidden="true"><circle cx="8" cy="8" r="6.5" fill="none" stroke="#444" stroke-width="1.5"/><path d="M8 4v4l3 2" fill="none" stroke="#444" stroke-width="1.5"/></svg></div>
<div class="form-field area" style="left:289px;top:3850px;width:622px;height:117px">Additional Info :</div>

<div class="btn btn-dark btn-appoint">Make Appointment
  <svg width="26" height="14" viewBox="0 0 26 14" aria-hidden="true"><path d="M0 7h24M18 1l6 6-6 6" fill="none" stroke="var(--white)" stroke-width="2"/></svg></div>

<!-- FOOTER -->
<footer class="footer">Copyright ©&nbsp;<b>STEADY LEDGER</b>&nbsp;- 2018 . All Right Reserved
  <span class="social" style="left:1000px"></span>
  <span class="social" style="left:1044px"></span>
  <span class="social" style="left:1088px"></span>
</footer>

</body>
</html>
```